Business Card Design

Online clothing womens clothing store, I sell my clothing online and at the markets.

i would like the attached picture on the front of the card and the contact information on the back.

Industry/Entity Type

Business

Contact Information for Business Card

Velvet Harbour
Marnie Talbot
(Instagram symbol) _velvet_harbour_
(Facebook symbol) www.facepage-example.com/velvetharbourau/

W : www.velvetharbour-example.com.au
E : info@velvetharbour-example.com.au
P : 0491876324

```html
<!DOCTYPE html>
<html lang="en">
<head>
<meta charset="utf-8">
<title>Velvet Harbour – Business Card</title>
<link rel="stylesheet" href="https://fonts.googleapis.com/css2?family=Barlow:wght@300;400&family=Arimo:wght@400&display=swap">
<style>
  :root {
    --page: #ece9e4;
    --card-black: #111112;
    --ink-white: #ffffff;
    --band-grey: #6f7275;
    --band-navy: #1a1f4a;
    --photo-light: #e9e6e1;
    --photo-mid: #b9ad9d;
    --photo-green: #8c9a6a;
    --banner: rgba(40, 40, 42, 0.78);
  }
  * { margin: 0; padding: 0; box-sizing: border-box; }
  html, body { width: 1200px; height: 892px; overflow: hidden; background: var(--page); }
  .canvas { position: relative; width: 1200px; height: 892px; }
  .card {
    position: absolute; left: 240px; width: 720px; height: 411px;
    overflow: hidden; box-shadow: 0 6px 18px rgba(0,0,0,0.18);
  }
  .card--front { top: 25px; }
  .card--back { top: 456px; background: var(--card-black); }

  /* front */
  .photo-area {
    position: absolute; inset: 0;
    background: linear-gradient(160deg, var(--photo-light) 0%, #d8d2c8 35%, var(--photo-mid) 60%, var(--photo-green) 100%);
  }
  .brand-banner {
    position: absolute; left: 0; top: 108px; width: 100%; height: 118px;
    background: var(--banner);
  }
  .brand-banner .brand-name {
    position: absolute; right: 40px; top: 34px;
    font: 300 48px/1 "Barlow", sans-serif; letter-spacing: 9px;
    color: var(--ink-white); white-space: nowrap;
  }

  /* back */
  .back-shapes { position: absolute; inset: 0; }
  .back-brand {
    position: absolute; left: 30px; top: 150px;
    font: 300 30px/1 "Barlow", sans-serif; letter-spacing: 6px;
    color: var(--ink-white); white-space: nowrap;
  }
  .divider { position: absolute; left: 378px; top: 60px; width: 2px; height: 218px; background: var(--ink-white); }
  .holder-name {
    position: absolute; left: 404px; top: 78px;
    font: 400 24px/1 "Barlow", sans-serif; letter-spacing: 4px; color: var(--ink-white);
  }
  .contact-list { position: absolute; left: 404px; top: 132px; list-style: none; }
  .contact-list li {
    display: flex; align-items: center; gap: 10px; height: 30px;
    font: 400 15px/1 "Arimo", sans-serif; color: var(--ink-white); white-space: nowrap;
  }
  .contact-list svg { width: 14px; height: 14px; flex: none; }
  .social-handle {
    position: absolute; left: 360px; top: 356px; display: flex; align-items: center; gap: 10px;
    font: 400 22px/1 "Arimo", sans-serif; color: var(--ink-white);
  }
  .square-mark { width: 18px; height: 18px; border: 2px solid var(--ink-white); }
</style>
</head>
<body>
<main class="canvas">

  <section class="card card--front" aria-label="Card front">
    <div class="photo-area" role="img" aria-label="Photograph of two women in boho outfits sitting on a sunny wooden porch step"></div>
    <div class="brand-banner">
      <span class="brand-name">VELVET HARBOUR</span>
    </div>
  </section>

  <section class="card card--back" aria-label="Card back">
    <svg class="back-shapes" width="720" height="411" viewBox="0 0 720 411" aria-hidden="true">
      <rect x="0" y="290" width="320" height="121" fill="var(--band-grey)"/>
      <path d="M250 411 L290 340 Q296 330 310 330 L720 330 L720 411 Z" fill="var(--band-navy)"/>
      <path d="M250 411 L290 340 Q296 330 310 330 L720 330" fill="none" stroke="var(--ink-white)" stroke-width="3"/>
    </svg>

    <div class="back-brand">VELVET HARBOUR</div>
    <div class="divider"></div>
    <div class="holder-name">Marnie Talbot</div>

    <ul class="contact-list">
      <li>
        <svg viewBox="0 0 14 14"><rect width="14" height="14" rx="2" fill="#fff"/><path d="M4 3 L6 3 L6.6 5.4 L5.4 6.2 Q6.2 7.9 7.8 8.6 L8.6 7.4 L11 8 L11 10 Q6 11 3 5 Z" fill="#111"/></svg>
        0491876324
      </li>
      <li>
        <svg viewBox="0 0 14 14"><rect width="14" height="14" rx="2" fill="#fff"/><rect x="2.5" y="4" width="9" height="6" fill="none" stroke="#111" stroke-width="1.2"/><path d="M2.5 4 L7 7.5 L11.5 4" fill="none" stroke="#111" stroke-width="1.2"/></svg>
        info@velvetharbour-example.com.au
      </li>
      <li>
        <svg viewBox="0 0 14 14"><rect width="14" height="14" rx="2" fill="#fff"/><circle cx="7" cy="7" r="4" fill="none" stroke="#111" stroke-width="1.2"/><path d="M3 7 H11 M7 3 Q4.5 7 7 11 M7 3 Q9.5 7 7 11" fill="none" stroke="#111" stroke-width="0.9"/></svg>
        www.velvetharbour-example.com.au
      </li>
      <li>
        <svg viewBox="0 0 14 14"><rect width="14" height="14" rx="2" fill="#fff"/></svg>
        velvetharbourau
      </li>
    </ul>

    <div class="social-handle"><span class="square-mark"></span>velvet_harbour</div>
  </section>

</main>
</body>
</html>
```